Silver Heron Low Voltage Systems New Van Wrap

We need a wrap for an Audio Video Company based in Orange County, CA. We design and install high end audio video systems for very expensive Residential home and large Commercial companies. We would like a design that speaks Quality, Simplicity, Clean, Elite and Professional. We are looking for a black and white design. (***All font needs to be Montserrat***) Our vans are white so graphic should be black. Less is more but we have to have the following information included:
Logo (See Attached)
Silver Heron
714-382-LINK
www.SilverHeron.pro
Commercial / Residential
Data * Fiber
Audio * Video
Security Systems
Please be sure to include a side and rear view of the vehicle. Thank you.
- Montserrat
- (***All font needs to be Montserrat***)
- Less is more but we have to have the following information included:
- Logo (See Attached)
- Silver Heron
- 714-382-LINK
- www.SilverHeron.pro
- Commercial / Residential
- Data * Fiber * Wi-Fi
- Audio * Video
- Security Systems

```html
<!DOCTYPE html>
<html lang="en">
<head>
<meta charset="utf-8">
<title>Silver Heron Low Voltage Systems – Van Wrap</title>
<link href="https://fonts.googleapis.com/css2?family=Montserrat:wght@400;600;700&display=swap" rel="stylesheet">
<style>
  :root {
    --wrap-black: #141414;
    --van-white: #ffffff;
    --panel-line: #d9d9d9;
    --page: #ffffff;
  }
  * { margin: 0; padding: 0; box-sizing: border-box; }
  html, body { width: 1200px; height: 400px; overflow: hidden; background: var(--page); }
  body { font-family: "Montserrat", sans-serif; color: var(--wrap-black); }
  .canvas { position: relative; width: 1200px; height: 400px; }

  .panel {
    position: absolute;
    background: var(--van-white);
    border: 1px solid var(--panel-line);
    border-radius: 14px;
  }
  .rear-panel { left: 56px; top: 56px; width: 218px; height: 210px; }
  .side-panel { left: 548px; top: 88px; width: 606px; height: 190px; border-radius: 18px; }

  .abs { position: absolute; }

  /* Rear view */
  .rear-window {
    left: 68px; top: 68px; width: 172px; height: 88px;
    background: var(--wrap-black);
    border-radius: 8px;
    display: flex; flex-direction: column; align-items: center; justify-content: center; gap: 8px;
  }
  .brand-dot { width: 22px; height: 22px; border-radius: 50%; background: var(--van-white); }
  .rear-window .brand-name { color: var(--van-white); font-weight: 700; font-size: 14px; letter-spacing: 0.2px; }
  .rear-phone { left: 72px; top: 158px; font-weight: 700; font-size: 17px; }
  .rear-services { left: 66px; top: 188px; font-size: 6.4px; line-height: 7.6px; }
  .rear-url { left: 152px; top: 222px; font-size: 7.4px; }

  /* Side view */
  .side-band {
    left: 568px; top: 100px; width: 318px; height: 68px;
    background: var(--wrap-black);
    border-radius: 4px;
    display: flex; align-items: center; justify-content: center;
  }
  .side-band .brand-name { color: var(--van-white); font-weight: 700; font-size: 31px; letter-spacing: 0.5px; }
  .side-phone { left: 568px; top: 170px; font-weight: 700; font-size: 23px; }
  .side-url { left: 749px; top: 177px; font-size: 11.5px; }
  .side-services { left: 727px; top: 216px; font-size: 7.4px; line-height: 9px; }
  .door-mark {
    left: 900px; top: 186px; width: 110px;
    display: flex; flex-direction: column; align-items: center; gap: 8px;
  }
  .door-mark .brand-dot { width: 40px; height: 40px; background: var(--wrap-black); }
  .door-mark .brand-name { font-weight: 700; font-size: 12px; white-space: nowrap; }
</style>
</head>
<body>
<main class="canvas">
  <section class="rear-view" aria-label="Rear view wrap">
    <div class="panel rear-panel"></div>
    <div class="abs rear-window">
      <span class="brand-dot"></span>
      <span class="brand-name">SILVER HERON</span>
    </div>
    <div class="abs rear-phone">714-382-LINK</div>
    <div class="abs rear-services">
      Audio * Video<br>Security Systems<br>Data * Fiber * Wi-Fi<br>Commercial / Residential
    </div>
    <div class="abs rear-url">www.SilverHeron.pro</div>
  </section>

  <section class="side-view" aria-label="Side view wrap">
    <div class="panel side-panel"></div>
    <div class="abs side-band"><span class="brand-name">SILVER HERON</span></div>
    <div class="abs side-phone">714-382-LINK</div>
    <div class="abs side-url">www.SilverHeron.pro</div>
    <div class="abs side-services">
      Audio * Video<br>Security Systems<br>Data * Fiber * Wi-Fi<br>Commercial / Residential
    </div>
    <div class="abs door-mark">
      <span class="brand-dot"></span>
      <span class="brand-name">SILVER HERON</span>
    </div>
  </section>
</main>
</body>
</html>
```